Design for Magento Sports ecommerce

Looking for a design (the PSD's only) for a web shop selling sports equipment.
We are using Magento but feel free to change any of the standard features/elements in Magento.
We are hoping to see something different and creative. Unlike the usual ecommerce designs from LayoutFalcon etc.

The main categories will be: Running (shoes, clothes etc), football (soccer), Handball, Cycling(equipment only), Fitness, Tennis and Swimming.
Lots of subcategories so easy navigation, like a dropdown, megamenu, might be an obvious choice.

The design should at least include suggestions for: Home Page, Product list, Product view and a CMS page (like About Us).

Hi everybody

Thanks for all the proposals on the project.
There're some really great ones and I appreciate the time and effort you all put into this.
I'm busy walking through each one and will get back as soon as possible.

Joris

Target Market(s)

Male & Females between 18-60. anyone doing sports in above categories.

Industry/Entity Type

Fitness

Requirements
Must have
• Filter/Layered Navigation is important. We use Kelvoro. See here:
http://www.kelvoro-demo.test/demo/seo-layered-navigation-plus/

Manufacturers logo on Product view page.

Related products / Upselling on Product view page.
Nice to have
• Product labels/stickers for marking New products, Special offer etc on Product List and Product View.

Icons instead of text links for Cart, My Account, sorting etc.

Responsive design that can make use of widescreen monitors as well as tablets.

The use of "handwriting" or handwritten icons, like here on drawquarry(sorry), looks awesome. :-)
Should not have
• you can disregard the following Magento features:
Wish list
Email a friend
Reviews

```html
<!DOCTYPE html>
<html lang="en">
<head>
<meta charset="utf-8">
<title>Kinetra – Sports Equipment Shop</title>
<link href="https://fonts.googleapis.com/css2?family=Oswald:wght@400;600;700&family=Roboto:wght@400;700&display=swap" rel="stylesheet">
<style>
:root{
  --blue:#1b8fd6;
  --blue-dark:#0f5f9c;
  --red:#d6211e;
  --red-dark:#9d1210;
  --ink:#222;
  --nav:#262626;
  --page:#e9e9e9;
  --line:#d3d3d3;
  --muted:#777;
  --foot:#2b2b2b;
  --foot-bar:#1c1c1c;
  --white:#fff;
}
*{box-sizing:border-box;margin:0;padding:0}
html,body{width:887px;height:1200px;overflow:hidden}
body{font-family:"Roboto",Arial,sans-serif;color:var(--ink);background:var(--page);position:relative;font-size:9px}
.abs{position:absolute}

/* header */
.site-header{left:0;top:0;width:887px;height:84px;background:var(--white)}
.logo{left:83px;top:14px}
.logo-name{font-family:"Oswald",Arial,sans-serif;font-weight:700;font-size:30px;color:var(--blue);line-height:1}
.account-links{right:74px;top:10px;display:flex;gap:14px;font-size:9px;color:#555;text-transform:uppercase;list-style:none}
.promise{left:445px;top:42px;font-family:"Oswald",Arial,sans-serif;font-weight:600;font-size:12px;letter-spacing:.3px}
.cart{left:632px;top:40px;display:flex;align-items:center;gap:6px;font-size:10px}
.cart-btn{background:var(--nav);color:var(--white);font-family:"Oswald",Arial,sans-serif;font-size:11px;padding:3px 8px;display:flex;align-items:center;gap:5px}
.cart-count{border:1px solid var(--line);padding:2px 5px}

/* nav */
.main-nav{left:0;top:84px;width:887px;height:24px;background:var(--nav)}
.nav-links{left:83px;top:0;height:24px;display:flex;align-items:center;gap:18px;font-family:"Oswald",Arial,sans-serif;color:var(--white);font-size:11px}
.search{left:560px;top:4px;display:flex;height:16px}
.search input{width:118px;border:0;height:16px;font-size:8px;padding:0 4px}
.search select{width:88px;border:0;border-left:1px solid var(--line);height:16px;font-size:8px}
.search button{width:44px;border:0;background:var(--red);color:var(--white);font-family:"Oswald",Arial,sans-serif;font-size:9px}

/* sidebar */
.sidebar{left:83px;top:120px;width:152px;height:614px;background:var(--white);border:1px solid var(--line)}
.sidebar-title{background:var(--nav);color:var(--white);font-family:"Oswald",Arial,sans-serif;font-size:10px;padding:3px 6px}
.sidebar-sub{background:#f2f2f2;border-bottom:1px solid var(--line);font-family:"Oswald",Arial,sans-serif;font-size:10px;padding:3px 6px;display:flex;justify-content:space-between}
.filter{position:relative;padding:4px 18px 6px 8px;border-bottom:1px solid var(--line)}
.filter h4{font-family:"Oswald",Arial,sans-serif;font-weight:600;font-size:10px;color:var(--blue);margin-bottom:3px;display:flex;align-items:center;gap:4px}
.filter h4::before{content:"";width:6px;height:6px;background:var(--blue)}
.filter li{list-style:none;font-size:8.5px;color:#444;height:13px;display:flex;align-items:center;gap:4px}
.filter li::before{content:"";width:7px;height:7px;border:1px solid #999;background:var(--white)}
.filter .scroll{position:absolute;right:6px;top:18px;bottom:6px;width:6px;background:#eee;border:1px solid #ccc}
.filter .scroll::after{content:"";position:absolute;left:0;right:0;top:0;height:40%;background:#555}
.swatch{width:18px;height:7px;display:inline-block}
.price-track{position:relative;height:6px;background:#ddd;border:1px solid #bbb;margin:6px 0}
.price-track i{position:absolute;left:10%;right:25%;top:0;bottom:0;background:var(--blue)}
.price-vals{display:flex;justify-content:space-between;font-size:8px;color:#555}

/* banner */
.hero{left:243px;top:120px;width:570px;height:216px;background:linear-gradient(135deg,#c41411 0%,#8f0d0b 100%)}
.hero-art{position:absolute;left:110px;top:70px;width:360px;height:140px;background:radial-gradient(ellipse at center,#f3f3f3 0%,#d9d9d9 45%,rgba(200,30,28,0) 72%)}
.hero-title{position:absolute;left:0;right:0;top:14px;text-align:center;color:var(--white);font-family:"Oswald",Arial,sans-serif;font-weight:700;font-size:30px;line-height:1.05}
.hero-title span{display:block;font-size:22px;font-weight:600}
.hero-arrow{position:absolute;top:95px;width:16px;height:26px;background:rgba(0,0,0,.35)}
.hero-dots{position:absolute;bottom:8px;left:50%;transform:translateX(-50%);display:flex;gap:4px}
.hero-dots i{width:7px;height:7px;border-radius:50%;background:#fff;opacity:.6}
.hero-dots i:first-child{opacity:1}

/* promos */
.promo{top:342px;height:54px;overflow:hidden}
.promo-sale{left:243px;width:282px;background:linear-gradient(90deg,#1877c3,#2aa2e6)}
.promo-sale .badge{position:absolute;left:8px;top:6px;color:var(--white);font-family:"Oswald",Arial,sans-serif;line-height:1}
.promo-sale .badge b{display:block;font-size:11px}
.promo-sale .badge strong{font-size:24px}
.promo-sale .badge small{font-size:10px}
.promo-sale .art{position:absolute;left:86px;top:4px;width:190px;height:46px;background:linear-gradient(90deg,#5a5a5a,#c8c8c8,#3f3f3f)}
.promo-news{left:531px;width:282px;background:linear-gradient(90deg,#181818,#3a3a3a)}
.promo-news .text{position:absolute;left:10px;top:5px;font-family:"Oswald",Arial,sans-serif;font-weight:700;line-height:1.05;color:var(--white);font-size:14px}
.promo-news .text span{display:block;color:var(--red);font-size:19px}
.promo-news .signup{position:absolute;right:8px;bottom:6px;background:var(--red);color:var(--white);font-family:"Oswald",Arial,sans-serif;font-size:9px;padding:2px 7px}

/* products */
.section-title{left:243px;width:570px;font-family:"Oswald",Arial,sans-serif;font-weight:600;font-size:15px;color:var(--blue);border-bottom:2px solid var(--line);padding-bottom:3px}
.grid{left:243px;width:570px;display:flex;gap:6px}
.card{flex:1;background:var(--white);border:1px solid var(--line);height:196px;padding:8px;position:relative}
.card .photo{height:96px;margin:0 6px 6px}
.card .name{font-size:8px;line-height:1.3;height:22px;color:#333}
.card .price{font-family:"Oswald",Arial,sans-serif;font-size:19px;color:var(--red);margin-top:10px}
.card .buy{display:flex;align-items:center;margin-top:6px;gap:3px}
.card .buy span{background:#eee;border:1px solid #bbb;font-family:"Oswald",Arial,sans-serif;font-size:9px;padding:2px 6px;color:#555}
.card .buy i{width:14px;height:14px;background:#eee;border:1px solid #bbb;display:inline-block}

/* footer */
.site-footer{left:0;top:930px;width:887px;height:240px;background:var(--foot);color:#bbb}
.foot-col{position:absolute;top:18px}
.foot-col h5{font-family:"Oswald",Arial,sans-serif;color:var(--white);font-size:10px;font-weight:600;margin-bottom:6px}
.foot-col li{list-style:none;font-size:8px;line-height:13px}
.newsletter p{font-size:8px;line-height:11px;width:180px}
.newsletter .field{display:flex;margin-top:6px}
.newsletter .field span{width:140px;height:16px;background:var(--white)}
.newsletter .field b{width:40px;height:16px;background:var(--red)}
.pay-badge{position:absolute;left:350px;top:150px;width:120px;height:32px;background:#3c3c3c}
.follow{position:absolute;left:560px;top:155px;display:flex;align-items:center;gap:6px;font-family:"Oswald",Arial,sans-serif;color:var(--white);font-size:11px}
.follow i{width:18px;height:18px;background:#555;display:inline-block}
.foot-bar{left:0;top:1170px;width:887px;height:30px;background:var(--foot-bar);color:#888;font-size:8px;padding:10px 83px}
</style>
</head>
<body>

<header class="abs site-header">
  <div class="abs logo"><span class="logo-name">Kinetra</span></div>
  <ul class="abs account-links"><li>Login</li><li>Register</li><li>My Account</li></ul>
  <div class="abs promise">FREE SHIPPING. FREE RETURNS</div>
  <div class="abs cart">
    <span class="cart-btn">
      <svg width="11" height="10" viewBox="0 0 11 10"><path d="M0 1h2l2 6h6l1-4H3" fill="none" stroke="#fff" stroke-width="1.2"/><circle cx="5" cy="9" r="1" fill="#fff"/><circle cx="9" cy="9" r="1" fill="#fff"/></svg>
      SHOPPING CART
    </span>
    <span class="cart-count">0</span><span>ITEMS</span>
  </div>
</header>

<nav class="abs main-nav">
  <div class="abs nav-links"><span>HOME</span><span>ABOUT US</span><span>PRODUCT</span><span>CONTACT</span></div>
  <form class="abs search">
    <input type="text" value="">
    <select><option>All Categories</option></select>
    <button type="button">SEARCH</button>
  </form>
</nav>

<aside class="abs sidebar">
  <div class="sidebar-title">SHOP BY</div>
  <div class="sidebar-sub"><span>SHOPPING OPTIONS</span><span>▾</span></div>
  <div class="filter" style="height:118px">
    <h4>CATEGORY</h4>
    <ul><li>Running (9)</li><li>Football (10)</li><li>Handball (7)</li><li>Cycling (5)</li><li>Fitness (8)</li><li>Tennis (6)</li><li>Swimming (4)</li></ul>
    <div class="scroll"></div>
  </div>
  <div class="filter" style="height:104px">
    <h4>BRANDS</h4>
    <ul><li>Brands name</li><li>Brands name</li><li>Brands name</li><li>Brands name</li><li>Brands name</li><li>Brands name</li></ul>
    <div class="scroll"></div>
  </div>
  <div class="filter" style="height:104px">
    <h4>MANUFACTURER</h4>
    <ul><li>Lorem Ipsum</li><li>Lorem Ipsum</li><li>Lorem Ipsum</li><li>Lorem Ipsum</li><li>Lorem Ipsum</li><li>Lorem Ipsum</li></ul>
    <div class="scroll"></div>
  </div>
  <div class="filter" style="height:66px">
    <h4>PRICE</h4>
    <div class="price-track"><i></i></div>
    <div class="price-vals"><span>£0</span><span>£500</span></div>
  </div>
  <div class="filter" style="height:146px">
    <h4>COLOUR</h4>
    <ul>
      <li><span class="swatch" style="background:#111"></span>Black (10)</li>
      <li><span class="swatch" style="background:#1b5fc4"></span>Blue (14)</li>
      <li><span class="swatch" style="background:#fff;border:1px solid #ccc"></span>White (6)</li>
      <li><span class="swatch" style="background:#d6211e"></span>Red (8)</li>
      <li><span class="swatch" style="background:#f1d21a"></span>Yellow (3)</li>
      <li><span class="swatch" style="background:#f28a1a"></span>Orange (5)</li>
      <li><span class="swatch" style="background:#3aa23a"></span>Green (2)</li>
    </ul>
    <div class="scroll"></div>
  </div>
</aside>

<section class="abs hero">
  <div class="hero-art" role="img" aria-label="Team jerseys, football boots and a ball arranged in a group"></div>
  <h1 class="hero-title">GREAT DEALS ON<span>THE BEST BRANDS</span></h1>
  <span class="hero-arrow" style="left:0"></span>
  <span class="hero-arrow" style="right:0"></span>
  <div class="hero-dots"><i></i><i></i><i></i><i></i></div>
</section>

<div class="abs promo promo-sale">
  <div class="badge"><b>UP TO</b><strong>75%</strong> <small>OFF</small></div>
  <div class="art" role="img" aria-label="Row of sports t-shirts on hangers"></div>
</div>
<div class="abs promo promo-news">
  <div class="text">GET OFFERS &amp; UPDATES<span>SPECIAL OFFERS</span></div>
  <span class="signup">SIGN UP</span>
</div>

<h2 class="abs section-title" style="top:404px">FEATURED PRODUCTS</h2>
<div class="abs grid" style="top:440px">
  <article class="card">
    <div class="photo" role="img" aria-label="White and black football" style="background:radial-gradient(circle,#f4f4f4 0%,#bdbdbd 55%,#fff 57%)"></div>
    <p class="name">Velox Trainer 4.10 Ball Training Ball</p>
    <p class="price">£20.00</p>
    <div class="buy"><span>ADD TO CART</span><i></i></div>
  </article>
  <article class="card">
    <div class="photo" role="img" aria-label="Grey sports t-shirt" style="background:linear-gradient(180deg,#fff,#cfcfcf 40%,#a9a9a9)"></div>
    <p class="name">Stridon Graphic Logo Tee, Running Tops</p>
    <p class="price">£15.99</p>
    <div class="buy"><span>ADD TO CART</span><i></i></div>
  </article>
  <article class="card">
    <div class="photo" role="img" aria-label="Yellow and orange match ball" style="background:radial-gradient(circle,#f7d23a 0%,#e6762a 52%,#fff 54%)"></div>
    <p class="name">Korvax Match Pro Volley Handball</p>
    <p class="price">£30.00</p>
    <div class="buy"><span>ADD TO CART</span><i></i></div>
  </article>
  <article class="card">
    <div class="photo" role="img" aria-label="Black running shorts" style="background:linear-gradient(180deg,#fff,#3a3a3a 30%,#111)"></div>
    <p class="name">Stridon Essential Run Shorts 5in</p>
    <p class="price">£13.00</p>
    <div class="buy"><span>ADD TO CART</span><i></i></div>
  </article>
</div>

<h2 class="abs section-title" style="top:662px">SPECIALS</h2>
<div class="abs grid" style="top:698px">
  <article class="card">
    <div class="photo" role="img" aria-label="Pink silicone swimming cap" style="background:radial-gradient(ellipse at 50% 60%,#f26aa0 0%,#c2346e 50%,#fff 52%)"></div>
    <p class="name">Aquilo Lake Swimming Cap Silicone</p>
    <p class="price">£24.00</p>
    <div class="buy"><span>ADD TO CART</span><i></i></div>
  </article>
  <article class="card">
    <div class="photo" role="img" aria-label="Red tennis racket" style="background:radial-gradient(ellipse at 50% 35%,#fff 25%,#d6211e 28%,#d6211e 36%,#fff 39%)"></div>
    <p class="name">Ravent Tour 100 Tennis Racket</p>
    <p class="price">£18.99</p>
    <div class="buy"><span>ADD TO CART</span><i></i></div>
  </article>
  <article class="card">
    <div class="photo" role="img" aria-label="Exercise bike" style="background:linear-gradient(180deg,#fff,#9a9a9a 50%,#555)"></div>
    <p class="name">Stridon Home Fit Exercise Bike Trainer</p>
    <p class="price">£20.00</p>
    <div class="buy"><span>ADD TO CART</span><i></i></div>
  </article>
  <article class="card">
    <div class="photo" role="img" aria-label="Blue swimming cap and goggles" style="background:radial-gradient(ellipse at 50% 55%,#8ec8ee 0%,#2a7fc2 50%,#fff 52%)"></div>
    <p class="name">Aquilo Jet Junior Swim Goggles + Cap</p>
    <p class="price">£12.00</p>
    <div class="buy"><span>ADD TO CART</span><i></i></div>
  </article>
</div>

<footer class="abs site-footer">
  <div class="foot-col" style="left:83px">
    <h5>ABOUT US</h5>
    <ul><li>Contact</li><li>About us</li><li>Blog</li><li>Sitemap</li></ul>
  </div>
  <div class="foot-col" style="left:200px">
    <h5>USEFUL INFORMATION</h5>
    <ul><li>Privacy and Security Policy</li><li>Cancellation &amp; Returns Policy</li><li>Terms and conditions</li><li>Sports Guide Brand's Guide</li><li>100% safe shopping</li></ul>
  </div>
  <div class="foot-col" style="left:350px">
    <h5>CUSTOMER SERVICE</h5>
    <ul><li>Register Now</li><li>Login</li><li>Contact us</li><li>FAQ</li><li>Free Shipping</li><li>Payment Methods</li><li>Returns / Feedback</li></ul>
  </div>
  <div class="foot-col newsletter" style="left:560px">
    <h5>EMAIL SIGN-UP</h5>
    <p>Sign up for our email and get special offers, new arrivals and news first, right to your inbox.</p>
    <div class="field"><span></span><b></b></div>
  </div>
  <div class="pay-badge" aria-label="Secure payment badge" role="img"></div>
  <div class="follow">FOLLOW US <i></i><i></i><i></i></div>
</footer>
<div class="abs foot-bar">Copyright © 2013 Kinetra Ltd. All Rights Reserved.</div>

</body>
</html>
```